business card design

i would like business cards designed. My business provides trade qualified personnel to the mining industry to work on heavy mobile equipment.
please put a excavator(digger) in the background in one design and have one design without so i can compare the difference.
also add info:
my logo(attached) and "mobile equipment repair and maintenance"
name: Gavin Stroud
address: 42 Brindle RD Ashmere Vale WX.
mobile: 0461902738
email: gavin@hollowvex.com

```html
<!DOCTYPE html>
<html lang="en">
<head>
<meta charset="utf-8">
<title>Hollowvex business cards</title>
<link href="https://fonts.googleapis.com/css2?family=Arimo:wght@400;700&display=swap" rel="stylesheet">
<style>
  :root{
    --paper:#ffffff;
    --navy:#0c2347;
    --navy-deep:#081c3a;
    --accent:#3f6fc4;
    --sky:#2a9fd8;
    --ink:#1a1a1a;
    --tagline:#ffffff;
  }
  *{margin:0;padding:0;box-sizing:border-box}
  html,body{width:1200px;height:788px;overflow:hidden}
  body{
    background:linear-gradient(180deg,#d4d4d4,#b6b6b6);
    font-family:"Arimo",Arial,sans-serif;
    position:relative;
  }
  .card{
    position:absolute;
    width:520px;height:318px;
    border-radius:22px;
    overflow:hidden;
    box-shadow:0 14px 30px rgba(0,0,0,.28);
  }
  .card-front{left:50px;top:235px;background:var(--paper)}
  .card-front .edge-band{
    position:absolute;left:0;right:0;bottom:0;height:7px;
    background:var(--accent);
  }
  .brand-name{
    position:absolute;left:38px;top:52px;
    font-size:44px;font-weight:700;letter-spacing:1px;
    color:var(--navy);text-transform:uppercase;
  }
  .person{position:absolute;left:38px;top:128px}
  .person-name{font-size:25px;font-weight:700;color:var(--navy);letter-spacing:.5px}
  .person-role{font-size:18px;color:var(--accent);margin-top:3px}
  .divider{
    position:absolute;left:38px;right:30px;top:196px;height:1.5px;
    background:var(--accent);
  }
  .contacts{position:absolute;left:38px;top:212px;list-style:none}
  .contacts li{
    display:flex;align-items:center;gap:8px;
    font-size:14px;color:var(--ink);line-height:22px;
  }
  .contacts svg{width:12px;height:12px;fill:var(--accent);flex:none}
  .address{
    position:absolute;right:30px;top:222px;text-align:right;
    font-size:14px;line-height:20px;color:var(--ink);
  }
  .card-back{
    left:630px;top:235px;
    background:linear-gradient(160deg,var(--navy) 0%,var(--navy-deep) 100%);
  }
  .back-brand{
    position:absolute;left:0;right:0;top:92px;text-align:center;
    font-size:64px;font-weight:700;letter-spacing:2px;
    color:var(--sky);text-transform:uppercase;
  }
  .tagline{
    position:absolute;left:0;right:0;top:222px;text-align:center;
    font-size:19px;color:var(--tagline);
  }
</style>
</head>
<body>

<section class="card card-front" aria-label="Business card front">
  <div class="brand-name">Hollowvex</div>
  <div class="person">
    <div class="person-name">GAVIN STROUD</div>
    <div class="person-role">Managing director</div>
  </div>
  <div class="divider"></div>
  <ul class="contacts">
    <li><svg viewBox="0 0 24 24" aria-hidden="true"><path d="M6.6 10.8a15 15 0 0 0 6.6 6.6l2.2-2.2a1 1 0 0 1 1-.25 11.4 11.4 0 0 0 3.6.57 1 1 0 0 1 1 1V20a1 1 0 0 1-1 1A17 17 0 0 1 3 4a1 1 0 0 1 1-1h3.5a1 1 0 0 1 1 1c0 1.25.2 2.45.57 3.6a1 1 0 0 1-.25 1z"/></svg>0461902738</li>
    <li><svg viewBox="0 0 24 24" aria-hidden="true"><path d="M2 5h20v14H2zM3.5 6.5 12 13l8.5-6.5z"/></svg>gavin@hollowvex.com</li>
    <li><svg viewBox="0 0 24 24" aria-hidden="true"><circle cx="12" cy="12" r="10"/></svg>www.hollowvex.com</li>
  </ul>
  <div class="address">42 Brindle RD<br>Ashmere Vale WX.</div>
  <div class="edge-band"></div>
</section>

<section class="card card-back" aria-label="Business card back">
  <div class="back-brand">Hollowvex</div>
  <div class="tagline">Mobile Equipment Repair &amp; Maintenance</div>
</section>

</body>
</html>
```